Family Farm Looking for meat label

We have a small farm in Italy with two types of cow "Piemontese" and "Pezzata Rossa Valdostana". We need label ( about 5x5 cm) to put on the boxes and on every single piece of meat.

Target Market(s)

private client

Industry/Entity Type

family farm

Colors

Designer to choose colors to be used in the design.

Requirements
Must have
• to write "Azienda Agricola Il Roveto" and the cow like our cow not differently. the Piemontese breed cow has the typical physical shapes as in the photo. No photo on the label just a drawing o something like that.
Nice to have
• just a one label, clear, fine and clean . Maybe with pastel color or watercolor. We are a small family farm.
Should not have
• no photo, no another type of cow

```html
<!DOCTYPE html>
<html lang="it">
<head>
<meta charset="utf-8">
<title>Azienda Agricola Il Roveto – Etichetta</title>
<link rel="stylesheet" href="https://fonts.googleapis.com/css2?family=Roboto:wght@700;900&display=swap">
<style>
  :root {
    --farm-green: #31b254;
    --label-white: #ffffff;
    --page-bg: #ffffff;
  }
  html, body {
    margin: 0;
    padding: 0;
    width: 1200px;
    height: 871px;
    overflow: hidden;
    background: var(--page-bg);
  }
  .canvas {
    position: relative;
    width: 1200px;
    height: 871px;
  }
  .meat-label {
    position: absolute;
    left: 381px;
    top: 216px;
    width: 438px;
    height: 438px;
    display: block;
  }
  .label-bg { fill: var(--farm-green); }
  .roof-white { fill: var(--label-white); }
  .roof-line {
    fill: none;
    stroke: var(--farm-green);
    stroke-width: 10;
    stroke-linejoin: miter;
  }
  .deco-ring {
    fill: none;
    stroke: var(--label-white);
    stroke-width: 10;
  }
  .farm-title {
    font-family: "Roboto", Arial, sans-serif;
    font-weight: 900;
    font-size: 73px;
    fill: var(--label-white);
    text-anchor: middle;
  }
  .brand-name {
    font-family: "Roboto", Arial, sans-serif;
    font-weight: 900;
    font-size: 98px;
    fill: var(--farm-green);
  }
  .brand-dot {
    fill: none;
    stroke: var(--farm-green);
    stroke-width: 4;
  }
</style>
</head>
<body>
<div class="canvas">
  <svg class="meat-label" viewBox="0 0 828 828" xmlns="http://www.w3.org/2000/svg">
    <rect class="label-bg" x="0" y="0" width="828" height="828"/>

    <circle class="deco-ring" cx="753" cy="65" r="32"/>
    <circle class="deco-ring" cx="69" cy="398" r="32"/>

    <text class="farm-title" x="410" y="182">AZIENDA AGRICOLA</text>
    <text class="farm-title" x="410" y="267">IL ROVETO</text>

    <polygon class="roof-white" points="0,549 315,366 828,662 828,828 0,828"/>
    <polyline class="roof-line" points="0,572 315,393 828,688"/>
    <polygon class="roof-white" points="525,445 828,619 828,632 525,458"/>

    <circle class="brand-dot" cx="338" cy="554" r="15"/>
    <text class="brand-name" x="93" y="728">IL ROVETO</text>
  </svg>
</div>
</body>
</html>
```